Tattoo Artist needs a personal business card designed

I am looking for a classy, clean, but antique feeling business card for myself that matches the theme and vibe of my tattoo shop. I would like to see a couple different options but we can go with an all black background, to start. I would like to see some western metallic lettering and deep/dark red accents. Maybe try adding a few with a mix of white fonts too. I would like to see the Shop's name and location which is Copper Lantern Ink, 4862 W. Delmora Rd. Tampa FL. 33617 Our tattoo shop has a western antique vibe, yet its classy and professional. We have a website you can see the color scheme and grab anymore information for designing this business card from: www.copperlanternink-studio.example - and if you want to add the website to the card. I would like my personal IG handle somewhere small with a unique and cleaner IG logo next to the name. My IG handle is: @dianekessoink I am basically trying to look for multiple ideas/concepts that will match best with our website and sticker. (Which I will upload in the files) I would like it to be very clean, simple, classy, but have a western traditional tattooing feel to it. Like an antique stores business card. Add whatever information you think would be best, since I am not the professional graphic designer.
Shop Name: Copper Lantern Ink
Location: 4862 W Delmora Rd Tampa FL 33617
Website: www.copperlanternink-studio.example
Number: 813 555 0187
My Personal IG: @dianekessoink

Thank you for taking your time to help me out with this project. Afterwards, I might need our studios website up for re-designing! So my end goal is to make everything intergraded with one another. I more likely need a logo too.

Target Market(s)

Professionals 35-55 years of age Male and Female
Firefighters, Military Service men and women

Contact Information for Business Card

All black background, with golden and red accents.
Traditional style, cowboy, western. Sharp, Clean, and Classy.

Requirements
Must have
• Shop Name - Copper Lantern Ink
• Shop Location - 4862 W Delmora Rd Tampa FL 33617
• My Name - Diane Kesso
• UNIQUE IG LOGO along with My Instagram - @dianekessoink
• Number - 813 555 0187
Nice to have
• Gold metallic font
• Red accents
• Western Antique Oddity feel
• Might be nice to have the Website if it can work and fit in the space.

```html
<!DOCTYPE html>
<html lang="en">
<head>
<meta charset="utf-8">
<title>Copper Lantern Ink — Business Card</title>
<link rel="stylesheet" href="https://fonts.googleapis.com/css2?family=Cinzel:wght@400;700&family=Lato:wght@400;700&display=swap">
<style>
  :root {
    --backdrop: #e9e4dc;
    --card-black: #161616;
    --gold: #d8ad52;
    --deep-red: #c40c0c;
    --ink-white: #f2f2f2;
    --muted-grey: #bdbdbd;
  }
  * { margin: 0; padding: 0; box-sizing: border-box; }
  html, body {
    width: 1200px; height: 900px; overflow: hidden;
    background: var(--backdrop);
  }
  .stage { position: relative; width: 1200px; height: 900px; }
  .card {
    position: absolute;
    width: 525px; height: 300px;
    background: var(--card-black);
    border-radius: 4px;
    box-shadow: 0 10px 28px rgba(0,0,0,0.28);
    overflow: hidden;
  }
  .card-front { left: 110px; top: 150px; }
  .card-back { left: 565px; top: 450px; }

  .front-name {
    position: absolute; left: 0; right: 0; top: 0; bottom: 0;
    display: flex; align-items: center; justify-content: center;
    font-family: "Cinzel", serif; font-weight: 700;
    font-size: 34px; letter-spacing: 4px;
    color: var(--gold); text-transform: uppercase;
  }

  .back-mark {
    position: absolute; right: 34px; top: 48px;
    font-family: "Cinzel", serif; font-weight: 700;
    font-size: 15px; letter-spacing: 2px;
    color: var(--gold); text-transform: uppercase;
  }
  .artist-name {
    position: absolute; left: 36px; top: 58px;
    font-family: "Cinzel", serif; font-weight: 700;
    font-size: 21px; letter-spacing: 1.5px;
    color: var(--gold); text-transform: uppercase;
  }
  .contact-list {
    position: absolute; left: 36px; top: 132px;
    list-style: none;
    font-family: "Lato", sans-serif; font-size: 14px;
    color: var(--ink-white); line-height: 22px;
  }
  .contact-list li { display: flex; align-items: center; gap: 7px; }
  .contact-icon { width: 13px; height: 13px; flex: none; }
  .address {
    position: absolute; left: 36px; top: 190px;
    font-family: "Lato", sans-serif; font-size: 14.5px;
    line-height: 21px; color: var(--muted-grey);
  }
  .wave { position: absolute; left: 0; top: 0; width: 525px; height: 300px; }
  .social-handle {
    position: absolute; right: 26px; top: 168px;
    display: flex; align-items: center; gap: 6px;
    font-family: "Lato", sans-serif; font-size: 13px;
    color: var(--ink-white);
  }
  .social-dot {
    width: 15px; height: 15px; border-radius: 50%;
    background: var(--ink-white);
  }
</style>
</head>
<body>
<main class="stage">
  <section class="card card-front" aria-label="Card front">
    <h1 class="front-name">Copper Lantern Ink</h1>
  </section>

  <section class="card card-back" aria-label="Card back">
    <svg class="wave" viewBox="0 0 525 300" aria-hidden="true">
      <path d="M0,246 C130,242 270,215 392,158 C285,214 140,252 0,262 Z" fill="var(--deep-red)"/>
      <path d="M0,270 C150,262 300,228 405,172 C450,148 490,128 525,116 L525,300 L0,300 Z" fill="var(--gold)"/>
    </svg>

    <div class="back-mark">Copper Lantern Ink</div>
    <h2 class="artist-name">Diane Kesso</h2>

    <ul class="contact-list">
      <li>
        <svg class="contact-icon" viewBox="0 0 16 16" aria-hidden="true">
          <path d="M3 2 L6 2 L7 5 L5.5 6.5 C6.5 8.5 7.5 9.5 9.5 10.5 L11 9 L14 10 L14 13 C14 14 13 14 12 14 C6.5 13.5 2.5 9.5 2 4 C2 3 2 2 3 2 Z" fill="var(--gold)"/>
        </svg>
        813 555 0187
      </li>
      <li>
        <svg class="contact-icon" viewBox="0 0 16 16" aria-hidden="true">
          <circle cx="8" cy="8" r="7" fill="var(--gold)"/>
          <path d="M1.5 8 H14.5 M8 1.5 C5 5 5 11 8 14.5 M8 1.5 C11 5 11 11 8 14.5" stroke="var(--card-black)" stroke-width="1.1" fill="none"/>
        </svg>
        www.copperlanternink-studio.example
      </li>
    </ul>

    <address class="address" style="font-style: normal;">
      Copper Lantern Ink 4862<br>W Delmora Rd Tampa FL 33617
    </address>

    <div class="social-handle">
      <span class="social-dot" aria-hidden="true"></span>
      @dianekessoink
    </div>
  </section>
</main>
</body>
</html>
```